We need a flyer for our company. We test drugs, laser, LED or other light sources for phototoxicity on healthy volunteers.
You can use our website for an idea or imagine www.lumivanta.co.uk
Lumivanta has a well-established reputation in the field of drug- and chemical-induced phototoxicity and expertise in clinical studies of photoprotective agents, such as nutraceuticals and antioxidants and light-based device development and application. The team at Lumivanta has an international reputation in the field of UV and visible light measurement and our team has a truly multidisciplinary nature, with professionals including physicians, medical physicists, biochemists, technicians and nurses.

Target Market(s)

any pharmaceutical or cosmetical company

Industry/Entity Type

Cosmetic

Font styles to use
Serif

Colors

Designer to choose colors to be used in the design.

Requirements
Must have
• Clinical studies:
• Phototoxicity
• Photoallergy to topical agents
• Photoprotection by oral or topical agents
• Light-based devices
• Laboratory studies:
• Photosafety and photoxicity
• Photophysics and light source evaluation
Nice to have
• Can you reduce the amount of text and concentrate on this point?
• First page:
• • Lumivanta has a well-established reputation in the field of drug- and chemical-induced phototoxicity and expertise in clinical studies of photoprotective agents:
• such as nutraceuticals
• and antioxidants
• and light-based device development and application.
• • The team at Lumivanta has an international reputation in the field of UV and visible light measurement and our team has a truly multidisciplinary nature, with professionals including physicians, medical physicists, biochemists, technicians and nurses
• Second page:
• Clinical studies
• Phototoxicity
• Light-based devices
• Laboratory studies

```html
<!DOCTYPE html>
<html lang="en">
<head>
<meta charset="utf-8">
<title>Lumivanta – Clinical Studies Flyer</title>
<link href="https://fonts.googleapis.com/css2?family=Arimo:wght@400&family=Lato:wght@700&display=swap" rel="stylesheet">
<style>
  :root {
    --page-bg: #2a2a2a;
    --sheet-light: #ffffff;
    --sheet-shade: #e4e4e4;
    --brand-blue: #155489;
    --brand-blue-light: #2a6aa3;
    --brand-blue-dark: #0f4272;
    --heading-blue: #1a5a92;
    --white: #ffffff;
  }
  * { box-sizing: border-box; margin: 0; padding: 0; }
  html, body {
    width: 1200px; height: 1200px; overflow: hidden;
    background: var(--page-bg);
  }
  .flyer {
    position: absolute; left: 180px; top: 23px;
    width: 840px; height: 1154px;
    background: radial-gradient(ellipse at 50% 55%, var(--sheet-light) 0%, var(--sheet-light) 35%, var(--sheet-shade) 100%);
  }
  .photo { position: absolute; }
  .photo--uv-lab { left: 51px; top: 53px; width: 362px; height: 248px;
    background: linear-gradient(135deg, #0a0d2a 0%, #2b2f7a 55%, #6a6fd0 70%, #161a3c 100%); }
  .photo--thermal-camera { left: 423px; top: 53px; width: 362px; height: 248px;
    background: linear-gradient(120deg, #6d6c6a 0%, #3a3634 45%, #b08a7a 70%, #2c2a2a 100%); }
  .photo--glassware { left: 53px; top: 865px; width: 234px; height: 170px;
    background: linear-gradient(160deg, #efe6d8 0%, #d9cdbb 50%, #f4f1ec 100%); }
  .photo--clinic-room { left: 301px; top: 865px; width: 235px; height: 170px;
    background: linear-gradient(180deg, #f1f3f4 0%, #d7dadc 60%, #9a9fa3 100%); }
  .photo--light-cabinet { left: 551px; top: 865px; width: 234px; height: 170px;
    background: radial-gradient(circle at 70% 45%, #f6d79a 0%, #b8793a 35%, #3a2410 75%, #140c05 100%); }

  .rule { position: absolute; height: 3px; background: var(--brand-blue); }
  .rule--top { left: 51px; top: 311px; width: 734px; }
  .rule--bottom { left: 53px; top: 853px; width: 730px; }

  .brand-plate {
    position: absolute; left: 260px; top: 252px; width: 309px; height: 92px;
    background: var(--white); border-radius: 14px;
  }
  .brand-plate__inner {
    position: absolute; left: 6px; top: 6px; right: 6px; bottom: 6px;
    background: var(--brand-blue); border-radius: 10px;
    display: flex; align-items: center; justify-content: center; gap: 16px;
  }
  .brand-plate__mark { width: 36px; height: 36px; background: var(--white); }
  .brand-plate__name {
    font-family: 'Lato', sans-serif; font-weight: 700; font-size: 38px;
    color: var(--white); letter-spacing: 0.5px;
  }

  .section-title {
    position: absolute; left: 0; width: 840px; text-align: center;
    font-family: 'Arimo', sans-serif; font-weight: 400;
    color: var(--heading-blue); font-size: 53px; line-height: 1;
  }
  .section-title--clinical { top: 355px; }
  .section-title--lab { top: 590px; }

  .tree { position: absolute; left: 0; top: 0; width: 840px; height: 1154px; pointer-events: none; }

  .study {
    position: absolute; height: 58px;
    border-radius: 9px;
    background: linear-gradient(180deg, var(--brand-blue-light) 0%, var(--brand-blue) 50%, var(--brand-blue-dark) 100%);
    box-shadow: 0 2px 3px rgba(0,0,0,0.25);
    display: flex; align-items: center; justify-content: center; text-align: center;
    font-family: 'Lato', sans-serif; font-weight: 700; color: var(--white);
    font-size: 13.5px; line-height: 1.2; text-transform: uppercase; padding: 0 8px;
  }
  .study--compact { font-size: 12.5px; line-height: 1.05; }
  .study--phototoxicity { left: 51px; top: 508px; width: 168px; }
  .study--photoallergy { left: 240px; top: 508px; width: 167px; }
  .study--photoprotection { left: 430px; top: 508px; width: 167px; }
  .study--devices { left: 620px; top: 508px; width: 167px; }
  .study--photosafety { left: 185px; top: 758px; width: 166px; height: 57px; }
  .study--photophysics { left: 477px; top: 758px; width: 167px; height: 57px; }

  .web-bar {
    position: absolute; left: 51px; top: 1049px; width: 734px; height: 50px;
    background: var(--brand-blue);
    display: flex; align-items: center; justify-content: center;
    font-family: 'Lato', sans-serif; font-weight: 700; font-size: 21px; color: var(--white);
  }
</style>
</head>
<body>
  <main class="flyer">
    <div class="photo photo--uv-lab" role="img" aria-label="Technician working under ultraviolet lamps in a dark laboratory"></div>
    <div class="photo photo--thermal-camera" role="img" aria-label="Hands holding a thermal imaging camera showing a heat image of a hand"></div>

    <div class="rule rule--top"></div>

    <div class="brand-plate">
      <div class="brand-plate__inner">
        <span class="brand-plate__mark"></span>
        <span class="brand-plate__name">Lumivanta</span>
      </div>
    </div>

    <h1 class="section-title section-title--clinical">CLINICAL STUDIES</h1>

    <svg class="tree" viewBox="0 0 840 1154" aria-hidden="true">
      <g fill="none" stroke="#155489" stroke-width="3" stroke-dasharray="9 6">
        <line x1="188" y1="420" x2="643" y2="420"/>
        <line x1="416" y1="420" x2="416" y2="469"/>
        <line x1="159" y1="469" x2="688" y2="469"/>
        <line x1="159" y1="469" x2="159" y2="507"/>
        <line x1="326" y1="469" x2="326" y2="507"/>
        <line x1="530" y1="469" x2="530" y2="507"/>
        <line x1="688" y1="469" x2="688" y2="507"/>

        <line x1="143" y1="654" x2="690" y2="654"/>
        <line x1="416" y1="654" x2="416" y2="712"/>
        <line x1="256" y1="712" x2="565" y2="712"/>
        <line x1="256" y1="712" x2="256" y2="757"/>
        <line x1="565" y1="712" x2="565" y2="757"/>
      </g>
    </svg>

    <div class="study study--phototoxicity">Phototoxicity</div>
    <div class="study study--photoallergy">Photoallergy<br>to topical agents</div>
    <div class="study study--photoprotection study--compact">Photoprotection<br>by oral or<br>topical agents</div>
    <div class="study study--devices">Light-based<br>devices</div>

    <h2 class="section-title section-title--lab">LABORATORY STUDIES</h2>

    <div class="study study--photosafety">Photosafety and<br>photoxicity</div>
    <div class="study study--photophysics study--compact">Photophysics and<br>light source<br>evaluation</div>

    <div class="rule rule--bottom"></div>

    <div class="photo photo--glassware" role="img" aria-label="Laboratory volumetric flasks capped with foil"></div>
    <div class="photo photo--clinic-room" role="img" aria-label="Clinical testing room with light exposure equipment"></div>
    <div class="photo photo--light-cabinet" role="img" aria-label="Lamp glowing inside a light test cabinet beside a colour spectrum"></div>

    <div class="web-bar">www.lumivanta.co.uk/clinical-studies</div>
  </main>
</body>
</html>
```